PICTURE CALENDAR - CONSTRUCTION COMPANY

- PICTURES CALENDAR 2018 (wall calendar) - graphic design - square 50 x 50 cm - 14 pages (title - months index pages) - languages ​​- german - Italian - construction industry - minimalistic and clear - modern - for each month inkluding logo color www.tovelbrunn.it
Updates

Project Deadline Extended
Reason: Sehr geehrte Damen und Herren, bitte um eine Fristverlängerung. Es ist Wochenende und ich selbst bekomme auf kein Feedback ob ein Design jetzt passt oder nicht. Weiters haben wir bereits einen Favoriten welcher aber noch Details abändern müsste. Vielen Dank! Mit freundlichen Grüßen, Matthias Kerber

Target Market(s)

construction worker

Industry/Entity Type

Construction

Font styles to use
Sans Serif

Colors
0355a3
dddddd

Requirements
Must have
• 49 x 49 cm 12 months german italiano short image description including logo
Nice to have
• cool line
Should not have
• the graphic design not playful, no gradients

```html
<!DOCTYPE html>
<html lang="de">
<head>
<meta charset="utf-8">
<title>Tovel Brunn – Bildkalender 2018</title>
<link rel="stylesheet" href="https://fonts.googleapis.com/css2?family=League+Gothic&family=Poppins:wght@300;500;600&display=swap">
<style>
  :root {
    --brand: #0355a3;
    --grey: #dddddd;
    --page: #ffffff;
    --stage: #ffffff;
    --text: #0355a3;
  }
  * { box-sizing: border-box; margin: 0; padding: 0; }
  html, body { width: 1200px; height: 1000px; overflow: hidden; background: var(--stage); }
  body { position: relative; font-family: "Poppins", sans-serif; color: var(--text); }

  .page {
    position: absolute;
    background: var(--page);
    border: 1px solid var(--grey);
    box-shadow: 0 0 6px rgba(0,0,0,.25);
  }
  .photo { position: absolute; }
  .photo--alpine { background: linear-gradient(180deg, #b9cde3 0%, #c8c6bd 32%, #6f8a63 50%, #7fb0a8 68%, #a48f6a 100%); }
  .photo--quarry { background: linear-gradient(180deg, #c7d4e2 0%, #4d6a45 40%, #a9a59c 70%, #8d8a82 100%); }
  .photo--slope { background: linear-gradient(160deg, #b8b3a8 0%, #8d8577 35%, #58704a 70%, #7b6c52 100%); }
  .photo--rock { background: linear-gradient(180deg, #a9c3de 0%, #cfcac0 45%, #9f9689 75%, #d8d2c8 100%); }
  .photo--road { background: linear-gradient(180deg, #a8c2dd 0%, #cfd9e0 35%, #6d8f55 60%, #6f6e6a 100%); }
  .photo--faded { background: linear-gradient(180deg, #eef2f8 0%, #dbe3ef 45%, #e9edf4 100%); }

  /* brand tag */
  .brand-tag { position: absolute; display: flex; align-items: center; gap: 6px; }
  .brand-tag__square { background: var(--brand); }
  .brand-tag__name { font-weight: 600; color: var(--brand); white-space: nowrap; }

  /* cover */
  .cover { left: 50px; top: 28px; width: 352px; height: 350px; }
  .cover .photo { inset: 0; }
  .cover .brand-tag { left: 100px; top: 150px; }
  .cover .brand-tag__square { width: 36px; height: 36px; }
  .cover .brand-tag__name { font-size: 21px; }
  .cover__year { position: absolute; left: 98px; top: 178px; font-weight: 600; font-size: 68px; color: var(--brand); opacity: .75; letter-spacing: 1px; }

  /* index */
  .index { left: 50px; top: 390px; width: 352px; height: 352px; }
  .index__grid { position: absolute; left: 26px; top: 43px; display: grid; grid-template-columns: repeat(4, 66px); column-gap: 12px; row-gap: 14px; }
  .index__item .photo { position: static; width: 66px; height: 43px; }
  .index__title { font-size: 4.6px; font-weight: 600; margin-top: 4px; line-height: 1.2; white-space: nowrap; }
  .index__text { font-size: 4px; font-weight: 300; line-height: 1.3; }
  .index .brand-tag { left: 26px; top: 290px; }
  .index .brand-tag__square { width: 28px; height: 28px; }
  .index .brand-tag__name { font-size: 14px; }

  /* month page */
  .month__badge { position: absolute; background: rgba(255,255,255,.82); display: flex; flex-direction: column; align-items: center; justify-content: center; }
  .month__badge-square { background: var(--brand); }
  .month__badge-year { font-weight: 600; color: var(--brand); }
  .month__name { position: absolute; font-family: "League Gothic", sans-serif; font-weight: 400; text-transform: uppercase; color: var(--brand); white-space: nowrap; }
  .month__rule { position: absolute; background: var(--brand); }
  .cal { position: absolute; display: grid; grid-template-columns: repeat(7, 1fr); text-align: center; font-weight: 300; color: var(--brand); }

  .month--large { left: 422px; top: 28px; width: 720px; height: 714px; }
  .month--large .photo { left: 52px; top: 40px; width: 615px; height: 410px; }
  .month--large .month__badge { left: 591px; top: 40px; width: 76px; height: 112px; gap: 6px; }
  .month--large .month__badge-square { width: 48px; height: 48px; }
  .month--large .month__badge-year { font-size: 19px; line-height: 1; }
  .month--large .month__name { left: 52px; top: 482px; font-size: 98px; line-height: 0.88; }
  .month--large .month__rule { left: 321px; top: 487px; width: 3px; height: 160px; }
  .month--large .cal { left: 390px; top: 483px; width: 280px; font-size: 15px; row-gap: 4.2px; line-height: 20px; }

  .month--small { top: 765px; height: 207px; }
  .month--small .photo { left: 17px; top: 17px; width: 172px; height: 113px; }
  .month--small .month__badge { left: 160px; top: 17px; width: 29px; height: 34px; gap: 2px; }
  .month--small .month__badge-square { width: 14px; height: 14px; }
  .month--small .month__badge-year { font-size: 6px; line-height: 1; }
  .month--small .month__name { left: 17px; top: 139px; font-size: 24px; line-height: 0.95; }
  .month--small .month__rule { left: 99px; top: 140px; width: 1px; height: 48px; }
  .month--small .cal { left: 106px; top: 140px; width: 86px; font-size: 5.5px; line-height: 7.2px; }

  .m1 { left: 48px; width: 206px; }
  .m2 { left: 271px; width: 208px; }
  .m3 { left: 493px; width: 209px; }
  .m4 { left: 715px; width: 203px; }
  .m5 { left: 931px; width: 207px; }
</style>
</head>
<body>

<section class="page cover">
  <div class="photo photo--faded" role="img" aria-label="Faded photo of an excavator on a gravel pile"></div>
  <div class="brand-tag"><span class="brand-tag__square"></span><span class="brand-tag__name">tovel brunn</span></div>
  <div class="cover__year">2018</div>
</section>

<section class="page index">
  <div class="index__grid">
    <div class="index__item"><div class="photo photo--road" role="img" aria-label="Road works truck"></div><p class="index__title">Description about the image</p><p class="index__text">Description about the image Description about the image.</p></div>
    <div class="index__item"><div class="photo photo--alpine" role="img" aria-label="Mountain reservoir construction"></div><p class="index__title">Description about the image</p><p class="index__text">Description about the image Description about the image.</p></div>
    <div class="index__item"><div class="photo photo--rock" role="img" aria-label="Excavator placing rocks"></div><p class="index__title">Description about the image</p><p class="index__text">Description about the image Description about the image.</p></div>
    <div class="index__item"><div class="photo photo--quarry" role="img" aria-label="Gravel site below forest"></div><p class="index__title">Description about the image</p><p class="index__text">Description about the image Description about the image.</p></div>
    <div class="index__item"><div class="photo photo--quarry" role="img" aria-label="Gravel site with machines"></div><p class="index__title">Description about the image</p><p class="index__text">Description about the image Description about the image.</p></div>
    <div class="index__item"><div class="photo photo--alpine" role="img" aria-label="Reservoir with dolomite peaks"></div><p class="index__title">Description about the image</p><p class="index__text">Description about the image Description about the image.</p></div>
    <div class="index__item"><div class="photo photo--slope" role="img" aria-label="Machines working on mountain site"></div><p class="index__title">Description about the image</p><p class="index__text">Description about the image Description about the image.</p></div>
    <div class="index__item"><div class="photo photo--rock" role="img" aria-label="Dump truck at rock wall"></div><p class="index__title">Description about the image</p><p class="index__text">Description about the image Description about the image.</p></div>
    <div class="index__item"><div class="photo photo--rock" role="img" aria-label="Excavator on slope"></div><p class="index__title">Description about the image</p><p class="index__text">Description about the image Description about the image.</p></div>
    <div class="index__item"><div class="photo photo--road" role="img" aria-label="Crushing machine on site"></div><p class="index__title">Description about the image</p><p class="index__text">Description about the image Description about the image.</p></div>
    <div class="index__item"><div class="photo photo--slope" role="img" aria-label="Excavator in forest clearing"></div><p class="index__title">Description about the image</p><p class="index__text">Description about the image Description about the image.</p></div>
    <div class="index__item"><div class="photo photo--slope" role="img" aria-label="Steep mountain slope works"></div><p class="index__title">Description about the image</p><p class="index__text">Description about the image Description about the image.</p></div>
  </div>
  <div class="brand-tag"><span class="brand-tag__square"></span><span class="brand-tag__name">tovel brunn</span></div>
</section>

<section class="page month month--large">
  <div class="photo photo--alpine" role="img" aria-label="Excavator loading a dump truck beside a mountain reservoir under dolomite peaks"></div>
  <div class="month__badge"><span class="month__badge-square"></span><span class="month__badge-year">2018</span></div>
  <h2 class="month__name">Juni<br>Giugno</h2>
  <div class="month__rule"></div>
  <div class="cal">
    <span>Mo</span><span>Di</span><span>Mi</span><span>Do</span><span>Fr</span><span>Sa</span><span>So</span>
    <span>Lu</span><span>Ma</span><span>Me</span><span>Gi</span><span>Ve</span><span>Sa</span><span>Do</span>
    <span style="grid-column-start:5">1</span><span>2</span><span>3</span>
    <span>4</span><span>5</span><span>6</span><span>7</span><span>8</span><span>9</span><span>10</span>
    <span>11</span><span>12</span><span>13</span><span>14</span><span>15</span><span>16</span><span>17</span>
    <span>18</span><span>19</span><span>20</span><span>21</span><span>22</span><span>23</span><span>24</span>
    <span>25</span><span>26</span><span>27</span><span>28</span><span>29</span><span>30</span>
  </div>
</section>

<section class="page month month--small m1">
  <div class="photo photo--quarry" role="img" aria-label="Gravel site with machines below a forested hill"></div>
  <div class="month__badge"><span class="month__badge-square"></span><span class="month__badge-year">2018</span></div>
  <h2 class="month__name">Januar<br>Gennaio</h2>
  <div class="month__rule"></div>
  <div class="cal">
    <span>Mo</span><span>Di</span><span>Mi</span><span>Do</span><span>Fr</span><span>Sa</span><span>So</span>
    <span>Lu</span><span>Ma</span><span>Me</span><span>Gi</span><span>Ve</span><span>Sa</span><span>Do</span>
    <span>1</span><span>2</span><span>3</span><span>4</span><span>5</span><span>6</span><span>7</span>
    <span>8</span><span>9</span><span>10</span><span>11</span><span>12</span><span>13</span><span>14</span>
    <span>15</span><span>16</span><span>17</span><span>18</span><span>19</span><span>20</span><span>21</span>
    <span>22</span><span>23</span><span>24</span><span>25</span><span>26</span><span>27</span><span>28</span>
    <span>29</span><span>30</span><span>31</span>
  </div>
</section>

<section class="page month month--small m2">
  <div class="photo photo--slope" role="img" aria-label="Machine on a steep rocky mountain slope"></div>
  <div class="month__badge"><span class="month__badge-square"></span><span class="month__badge-year">2018</span></div>
  <h2 class="month__name">November<br>Novembre</h2>
  <div class="month__rule"></div>
  <div class="cal">
    <span>Mo</span><span>Di</span><span>Mi</span><span>Do</span><span>Fr</span><span>Sa</span><span>So</span>
    <span>Lu</span><span>Ma</span><span>Me</span><span>Gi</span><span>Ve</span><span>Sa</span><span>Do</span>
    <span style="grid-column-start:4">1</span><span>2</span><span>3</span><span>4</span>
    <span>5</span><span>6</span><span>7</span><span>8</span><span>9</span><span>10</span><span>11</span>
    <span>12</span><span>13</span><span>14</span><span>15</span><span>16</span><span>17</span><span>18</span>
    <span>19</span><span>20</span><span>21</span><span>22</span><span>23</span><span>24</span><span>25</span>
    <span>26</span><span>27</span><span>28</span><span>29</span><span>30</span>
  </div>
</section>

<section class="page month month--small m3">
  <div class="photo photo--rock" role="img" aria-label="Excavator placing large rocks"></div>
  <div class="month__badge"><span class="month__badge-square"></span><span class="month__badge-year">2018</span></div>
  <h2 class="month__name">September<br>Settembre</h2>
  <div class="month__rule"></div>
  <div class="cal">
    <span>Mo</span><span>Di</span><span>Mi</span><span>Do</span><span>Fr</span><span>Sa</span><span>So</span>
    <span>Lu</span><span>Ma</span><span>Me</span><span>Gi</span><span>Ve</span><span>Sa</span><span>Do</span>
    <span style="grid-column-start:6">1</span><span>2</span>
    <span>3</span><span>4</span><span>5</span><span>6</span><span>7</span><span>8</span><span>9</span>
    <span>10</span><span>11</span><span>12</span><span>13</span><span>14</span><span>15</span><span>16</span>
    <span>17</span><span>18</span><span>19</span><span>20</span><span>21</span><span>22</span><span>23</span>
    <span>24</span><span>25</span><span>26</span><span>27</span><span>28</span><span>29</span><span>30</span>
  </div>
</section>

<section class="page month month--small m4">
  <div class="photo photo--quarry" role="img" aria-label="Gravel site with machines below a forested hill"></div>
  <div class="month__badge"><span class="month__badge-square"></span><span class="month__badge-year">2018</span></div>
  <h2 class="month__name">Dezember<br>Dicembre</h2>
  <div class="month__rule"></div>
  <div class="cal">
    <span>Mo</span><span>Di</span><span>Mi</span><span>Do</span><span>Fr</span><span>Sa</span><span>So</span>
    <span>Lu</span><span>Ma</span><span>Me</span><span>Gi</span><span>Ve</span><span>Sa</span><span>Do</span>
    <span style="grid-column-start:6">1</span><span>2</span>
    <span>3</span><span>4</span><span>5</span><span>6</span><span>7</span><span>8</span><span>9</span>
    <span>10</span><span>11</span><span>12</span><span>13</span><span>14</span><span>15</span><span>16</span>
    <span>17</span><span>18</span><span>19</span><span>20</span><span>21</span><span>22</span><span>23</span>
    <span>24</span><span>25</span><span>26</span><span>27</span><span>28</span><span>29</span><span>30</span>
    <span>31</span>
  </div>
</section>

<section class="page month month--small m5">
  <div class="photo photo--road" role="img" aria-label="Road sweeper truck on a country road with wildflowers"></div>
  <div class="month__badge"><span class="month__badge-square"></span><span class="month__badge-year">2018</span></div>
  <h2 class="month__name">März<br>Marzo</h2>
  <div class="month__rule"></div>
  <div class="cal">
    <span>Mo</span><span>Di</span><span>Mi</span><span>Do</span><span>Fr</span><span>Sa</span><span>So</span>
    <span>Lu</span><span>Ma</span><span>Me</span><span>Gi</span><span>Ve</span><span>Sa</span><span>Do</span>
    <span style="grid-column-start:4">1</span><span>2</span><span>3</span><span>4</span>
    <span>5</span><span>6</span><span>7</span><span>8</span><span>9</span><span>10</span><span>11</span>
    <span>12</span><span>13</span><span>14</span><span>15</span><span>16</span><span>17</span><span>18</span>
    <span>19</span><span>20</span><span>21</span><span>22</span><span>23</span><span>24</span><span>25</span>
    <span>26</span><span>27</span><span>28</span><span>29</span><span>30</span><span>31</span>
  </div>
</section>

</body>
</html>
```